"The Quiet Mirror" Musical Theatre Poster Design

Hi there! I need a poster design for a new youth musical I'm writing called "The Quiet Mirror".

The story is about a girl called Terri who is the most popular girl in the school. However, after a horrible accident, Terri is confined to a wheelchair. Not only does she have to deal with coming to terms with her life in a wheelchair, but she also has to make new friends after her old group of friends decide that she no longer fits their idea of 'perfect'. It's a powerful, modern story that uses contemporary music, technology but also hits at the heart of the teenage social experience.

Musically, the styles include pop, RnB, and pop/rock.

As for what I need in the poster - I'm not really sure! I'm looking for something that:
- uses the title "The Quiet Mirror" in a unique way
- doesn't necessarily use a wheelchair as an image
- would appeal to a 10-15 year old audience (so not too childish, more teen or tween), yet has a sense of seriousness to it. The musical is dramatic and deals with some confronting issues.
- includes "A New Musical by Maya Fitch"

As for colours, etc. surprise me! Sorry I can't be more specific but I haven't even really got a visual on it at all.

If you would like some demo recordings of the music, just let me know!

I've also attached some poster that I really like - more of a reference point of how a musical theatre poster should look.

Target Market(s)

Teens and adults

Font styles to use
Serif
Sans Serif

Colors

Designer to choose colors to be used in the design.

Requirements
Nice to have
• * perhaps use the concept of "different" and "normal" as two opposite yet somehow similar words.
• * maybe use of circles to symbolise a wheelchair but also having to start again, circular nature of life, rebirth, renewal?
Should not have
• - not any instruments in the design. The poster is for a theatrical musical, not a pop group, or singular song.

```html
<!DOCTYPE html>
<html lang="en">
<head>
<meta charset="utf-8">
<title>The Quiet Mirror – A New Musical</title>
<link rel="stylesheet" href="https://fonts.googleapis.com/css2?family=Arimo:wght@400;700&display=swap">
<style>
  :root {
    --page-bg: #e6e6e4;
    --poster-black: #050509;
    --ink-white: #ffffff;
    --glow-blue: #3b4fd8;
    --glow-violet: #8a3fc0;
    --glow-red: #c21e3a;
    --hair-red: #d8263a;
    --crowd-dark: #17171c;
  }
  html, body {
    margin: 0;
    padding: 0;
    width: 1200px;
    height: 831px;
    overflow: hidden;
    background: var(--page-bg);
  }
  .stage {
    position: relative;
    width: 1200px;
    height: 831px;
    display: flex;
    align-items: center;
    justify-content: center;
  }
  .poster {
    position: relative;
    width: 481px;
    height: 780px;
    background: var(--poster-black);
    overflow: hidden;
    box-shadow: 0 6px 24px rgba(0,0,0,0.25);
  }
  .poster-art {
    position: absolute;
    inset: 0;
    display: block;
  }
  .badge-text {
    font-family: "Arimo", Arial, sans-serif;
    font-weight: 400;
    fill: var(--ink-white);
  }
  .title {
    font-family: "Arimo", Arial, sans-serif;
    font-weight: 700;
    fill: var(--ink-white);
  }
</style>
</head>
<body>
<main class="stage">
  <section class="poster">
    <svg class="poster-art" viewBox="0 0 481 780" width="481" height="780" xmlns="http://www.w3.org/2000/svg">
      <defs>
        <radialGradient id="halo" cx="50%" cy="50%" r="50%">
          <stop offset="0%" stop-color="#1a0d22"/>
          <stop offset="72%" stop-color="#2a1030"/>
          <stop offset="86%" stop-color="var(--glow-violet)"/>
          <stop offset="93%" stop-color="var(--glow-blue)"/>
          <stop offset="100%" stop-color="var(--poster-black)" stop-opacity="0"/>
        </radialGradient>
        <linearGradient id="halo-tint" x1="0" y1="0" x2="1" y2="0">
          <stop offset="0%" stop-color="var(--glow-blue)" stop-opacity="0.45"/>
          <stop offset="55%" stop-color="var(--glow-violet)" stop-opacity="0.15"/>
          <stop offset="100%" stop-color="var(--glow-red)" stop-opacity="0.55"/>
        </linearGradient>
        <linearGradient id="singer" x1="0" y1="0" x2="0" y2="1">
          <stop offset="0%" stop-color="var(--hair-red)"/>
          <stop offset="60%" stop-color="#a42030"/>
          <stop offset="100%" stop-color="#5a1620"/>
        </linearGradient>
        <linearGradient id="crowd" x1="0" y1="0" x2="0" y2="1">
          <stop offset="0%" stop-color="var(--crowd-dark)"/>
          <stop offset="100%" stop-color="#000000"/>
        </linearGradient>
      </defs>

      <g class="hero-image" role="img" aria-label="Photo of a red-haired teenage girl singing with headphones, set inside a glowing blue and red ring of light against a starry night">
        <circle cx="244" cy="320" r="238" fill="url(#halo)"/>
        <circle cx="244" cy="320" r="215" fill="url(#halo-tint)"/>
        <ellipse cx="200" cy="470" rx="150" ry="180" fill="url(#singer)" opacity="0.55"/>
      </g>

      <g class="title-band">
        <path d="M0 557 Q 190 500 481 745 L 481 780 L 0 780 Z" fill="url(#crowd)" role="img" aria-label="Dim photo of a cheering concert crowd"/>
        <path d="M0 557 Q 190 500 481 745" fill="none" stroke="var(--ink-white)" stroke-width="2"/>
        <text class="title" x="40" y="635" font-size="74">THE</text>
        <text class="title" x="38" y="693" font-size="62">QUIET</text>
        <text class="title" x="36" y="756" font-size="78">MIRROR</text>
      </g>

      <g class="show-badge">
        <circle cx="361" cy="129" r="96" fill="var(--poster-black)"/>
        <circle cx="361" cy="129" r="87" fill="none" stroke="var(--ink-white)" stroke-width="2.5" stroke-dasharray="0.1 6" stroke-linecap="round"/>
        <text class="badge-text" x="361" y="122" font-size="18" text-anchor="middle">A NEW MUSICAL</text>
        <text class="badge-text" x="361" y="147" font-size="18" text-anchor="middle">by Maya Fitch</text>
      </g>
    </svg>
  </section>
</main>
</body>
</html>
```